Flyer-Design für Immobilienhändler
Zielgruppe
Ich bin ein kleiner Immobilienhändler (nebenberuflich, meine Frau und ich, 2-Mann Unternehmen) und kaufe direkt Wohnimmobilen (Haus/Wohnungen) ein, um diese aufzuwerten und dann wieder zu verkaufen. Ich bin kein Makler, habe aber ähnliche Zielgruppen wie ein Makler, nur mit dem Unterschied das ich die Immos direkt kostenfrei kaufe so wie sie sind! Zielgruppe sind bei mir Privatpersonen (im mittlerem-höherem Alter 50-80 Jahre) die Ihre Immobilie verkaufen möchten.
Aufgabenstellung
Es soll ein Flyer sein mit folgenden Vorgaben:
• Design: Modern, einfach und wichtig ist das es professional und sehr seriös wirkt
• Auf den ersten Blick sollte die Message verständlich sein was ich suche und was die Vorteile sind es bei mir zu verkaufen, anstatt das einem Makler zu übergeben (siehe mein Entwurf).
• Flyer Format z.B. DIN A5/A6, was sich gut versenden lässt. Vorschläge sind willkommen
Im Anhang habe ein einen eigenen Entwurf beigefügt, jedoch bin offen für komplett neue Vorschläge was Text und Design angeht.

```html
<!DOCTYPE html>
<html lang="de">
<head>
<meta charset="utf-8">
<title>Hausvero Flyer</title>
<link rel="stylesheet" href="https://fonts.googleapis.com/css2?family=Montserrat:wght@400;500;600;700;800&family=Roboto:wght@400;700&display=swap">
<style>
  :root {
    --yellow: #fcc900;
    --navy: #1d2236;
    --paper: #ffffff;
    --page: #ffffff;
  }
  * { margin: 0; padding: 0; box-sizing: border-box; }
  html, body { width: 1200px; height: 2744px; overflow: hidden; background: var(--page); }
  body { position: relative; color: var(--navy); font-family: "Roboto", Arial, sans-serif; }

  .flyer {
    position: absolute; left: 173px; width: 840px; height: 840px;
    background: var(--paper); overflow: hidden;
    box-shadow: 0 2px 8px rgba(0,0,0,0.18);
  }
  .flyer--front { top: 126px; }
  .flyer--back { top: 1069px; }

  .abs { position: absolute; }

  .brand {
    font-family: "Montserrat", Arial, sans-serif; font-weight: 600;
    font-size: 27px; letter-spacing: 1.5px; color: var(--navy);
    transform: translateX(-50%); white-space: nowrap;
  }

  /* front */
  .door-photo {
    left: 400px; top: 79px; width: 440px; height: 681px;
    background: linear-gradient(180deg, #b7b3ad 0%, #8e9194 30%, #5e6366 60%, #7a5e48 85%, #6b513d 100%);
  }
  .headline-box {
    left: 0; top: 139px; width: 495px; height: 273px; background: var(--yellow);
    padding: 45px 0 0 40px; font-family: "Montserrat", Arial, sans-serif;
  }
  .headline-kicker { font-size: 28px; font-weight: 500; line-height: 37px; }
  .headline-main { font-size: 49px; font-weight: 800; line-height: 54px; margin-top: 8px; }
  .benefits { left: 40px; top: 468px; list-style: none; }
  .benefits li {
    display: flex; align-items: center; height: 52.5px;
    font-size: 24px; color: var(--navy); white-space: nowrap;
  }
  .benefits svg { width: 20px; height: 16px; margin-right: 9px; }
  .contact-label { left: 92px; top: 720px; font-family: "Montserrat", Arial, sans-serif; font-size: 19px; }
  .contact-lines {
    left: 92px; top: 750px; font-family: "Montserrat", Arial, sans-serif;
    font-weight: 600; font-size: 29px; line-height: 31px;
  }
  .contact-icon { left: 40px; top: 758px; width: 40px; height: 48px; }

  /* back */
  .house-photo {
    left: 0; top: 112px; width: 420px; height: 682px;
    background: linear-gradient(180deg, #c9d6e4 0%, #aab4bd 20%, #e4e3df 40%, #8a6a4a 55%, #7d7a78 75%, #a49a8f 100%);
  }
  .section-title {
    left: 453px; font-size: 27px; font-weight: 700; color: var(--navy); white-space: nowrap;
  }
  .reasons { left: 439px; top: 207px; width: 390px; list-style: none; }
  .reasons li {
    position: relative; padding-left: 14px; font-size: 18.5px; line-height: 25px;
    margin-bottom: 17px;
  }
  .reasons li::before {
    content: ""; position: absolute; left: 0; top: 10px; width: 5px; height: 5px; background: var(--yellow);
  }
  .reasons b { font-weight: 700; }
  .steps { left: 453px; top: 578px; list-style: none; }
  .steps li { display: flex; align-items: center; height: 71px; }
  .step-num { position: relative; width: 68px; height: 50px; }
  .step-num svg { position: absolute; left: 0; top: 22px; width: 60px; height: 18px; }
  .step-num span {
    position: absolute; left: 16px; top: -2px; font-family: "Montserrat", Arial, sans-serif;
    font-weight: 800; font-size: 36px; color: var(--navy);
  }
  .step-text { font-family: "Montserrat", Arial, sans-serif; font-size: 19.5px; line-height: 23px; margin-left: 2px; }
</style>
</head>
<body>

<section class="flyer flyer--front">
  <div class="abs door-photo" role="img" aria-label="Foto: moderne graue Haustür mit Glaselementen, Holzterrasse und Ziergräsern"></div>
  <div class="abs brand" style="left:157px; top:78px;">HAUSVERO</div>
  <div class="abs headline-box">
    <div class="headline-kicker">SIE MÖCHTEN<br>IHRE IMMOBILIE</div>
    <div class="headline-main">ZUM BESTPREIS<br>VERKAUFEN?</div>
  </div>
  <ul class="abs benefits">
    <li><svg viewBox="0 0 20 16"><path d="M2 8 L8 13 L18 2" fill="none" stroke="var(--yellow)" stroke-width="4"/></svg>Wir sind keine Makler</li>
    <li><svg viewBox="0 0 20 16"><path d="M2 8 L8 13 L18 2" fill="none" stroke="var(--yellow)" stroke-width="4"/></svg>Ohne Renovierung/Sanierung</li>
    <li><svg viewBox="0 0 20 16"><path d="M2 8 L8 13 L18 2" fill="none" stroke="var(--yellow)" stroke-width="4"/></svg>Ohne Gebühren</li>
    <li><svg viewBox="0 0 20 16"><path d="M2 8 L8 13 L18 2" fill="none" stroke="var(--yellow)" stroke-width="4"/></svg>Ohne Besucherstress</li>
  </ul>
  <div class="abs contact-label">Unverbindliches Angebot</div>
  <svg class="abs contact-icon" viewBox="0 0 40 48" aria-hidden="true">
    <rect x="0" y="0" width="34" height="48" rx="4" fill="var(--yellow)"/>
    <rect x="34" y="8" width="6" height="10" fill="var(--yellow)"/>
    <rect x="34" y="22" width="6" height="10" fill="var(--yellow)"/>
    <path d="M10 14 c-2 4 0 12 8 17 l3-3 l4 3 l-2 4 c-9 -2 -16 -12 -15 -21 z" fill="var(--paper)"/>
  </svg>
  <div class="abs contact-lines">06021 48 37 15<br>info@hausvero.net</div>
</section>

<section class="flyer flyer--back">
  <div class="abs house-photo" role="img" aria-label="Foto: modernes Einfamilienhaus mit Satteldach, Balkon und Klinkerfassade"></div>
  <div class="abs brand" style="left:616px; top:72px;">HAUSVERO</div>
  <div class="abs section-title" style="top:145px;">WARUM MIT UNS?</div>
  <ul class="abs reasons">
    <li>Abkauf direkt von uns, zum fairen <b>Bestpreis</b></li>
    <li>Professionelle, schnelle und komplette Kaufabwicklung <b>aus einer Hand</b></li>
    <li>Sie brauchen nicht renovieren,<br>sanieren oder entrümpeln</li>
    <li><b>Keine Maklergebühr</b>, kein Besucherstress</li>
    <li><b>Kein Haftungsrisiko</b> - Wir kaufen Ihre Immobilie so wie sie ist</li>
  </ul>
  <div class="abs section-title" style="top:528px;">VERKAUFEN IN 3 SCHRITTEN</div>
  <ol class="abs steps">
    <li><div class="step-num"><svg viewBox="0 0 60 18"><polygon points="8,0 60,0 52,18 0,18" fill="var(--yellow)"/></svg><span>1</span></div><div class="step-text">Wir besichtigen Ihre<br>Immobilie im Detail</div></li>
    <li><div class="step-num"><svg viewBox="0 0 60 18"><polygon points="8,0 60,0 52,18 0,18" fill="var(--yellow)"/></svg><span>2</span></div><div class="step-text">Sie erhalten ein<br>Angebot von uns</div></li>
    <li><div class="step-num"><svg viewBox="0 0 60 18"><polygon points="8,0 60,0 52,18 0,18" fill="var(--yellow)"/></svg><span>3</span></div><div class="step-text">Wir kaufen Ihre<br>Immobilie &amp; zahlen</div></li>
  </ol>
</section>

</body>
</html>
```